Brightwell Power Systems

We'd like a web design that's beautiful and professional. We replace existing inefficient systems (mostly lighting at the moment but expanding) with highly efficient systems.

```html
<!DOCTYPE html>
<html lang="en">
<head>
<meta charset="utf-8">
<title>Brightwell Power Systems — LED Lighting Solutions</title>
<link rel="stylesheet" href="https://fonts.googleapis.com/css2?family=Open+Sans:wght@400;600;700&display=swap">
<style>
:root{
  --accent:#36b3bf;
  --accent-dark:#2a9ca7;
  --ink:#333538;
  --muted:#6d7075;
  --faint:#a4a7ab;
  --bar:#3b3e43;
  --band:#46484d;
  --soft:#f6f6f6;
  --line:#e3e4e6;
  --white:#ffffff;
}
*{box-sizing:border-box;margin:0;padding:0}
html,body{width:1200px;height:2219px;overflow:hidden}
body{font-family:"Open Sans",Arial,sans-serif;color:var(--ink);background:var(--white);font-size:13px;line-height:1.6;position:relative}
.wrap{width:890px;margin:0 auto;position:relative}
a{color:inherit;text-decoration:none}

/* top bar */
.topbar{height:26px;background:var(--bar);color:#c9cbce;font-size:11px}
.topbar .wrap{display:flex;justify-content:space-between;align-items:center;height:26px}
.topbar .contact{display:flex;align-items:center;gap:14px}
.topbar .contact b{color:#fff;font-weight:600}
.social{display:flex;gap:9px}
.social span{width:11px;height:11px;border-radius:50%;background:#8a8d92;display:block}

/* settings tab */
.settings{position:absolute;left:0;width:34px;height:34px;background:var(--band);display:flex;align-items:center;justify-content:center;z-index:3}

/* nav */
.nav{height:76px;background:var(--white);border-bottom:1px solid var(--line)}
.nav .wrap{display:flex;align-items:center;justify-content:space-between;height:76px}
.brand{display:flex;align-items:center;gap:8px;font-weight:700;font-size:15px;color:#1f7d3c}
.brand i{width:20px;height:20px;background:#1f7d3c;display:block}
.menu{display:flex;gap:0;height:76px;align-items:stretch}
.menu a{display:flex;align-items:center;padding:0 15px;font-size:13px;color:#3d4044;border-bottom:3px solid transparent}
.menu a.active{color:var(--accent);border-bottom-color:var(--accent)}

/* hero */
.hero{height:388px;background:linear-gradient(180deg,#f4f4f4 0%,#dcdcdc 100%);position:relative;overflow:hidden}
.hero .wrap{height:388px}
.hero h1{position:absolute;top:108px;left:0;font-size:36px;font-weight:600;color:#2e3033;letter-spacing:-.3px}
.hero p{position:absolute;top:160px;left:0;font-size:20px;color:#3c3e42}
.hero .lamps{position:absolute;left:400px;top:28px;width:520px;height:340px;border-radius:40px;background:radial-gradient(ellipse at 55% 55%,#fbfbfb 0%,#d9dadb 55%,rgba(220,220,220,0) 75%)}
.arrow{position:absolute;top:262px;width:26px;height:70px;background:#55585c;display:flex;align-items:center;justify-content:center}
.arrow.prev{left:18px}.arrow.next{right:18px}
.dots{position:absolute;left:560px;top:456px;display:flex;gap:5px}
.dots span{width:10px;height:10px;border-radius:50%;background:#9fa2a6}
.dots span.on{background:var(--accent)}

/* tagline */
.tagline{height:74px;background:var(--band);color:#e5e6e8;font-size:15px}
.tagline .wrap{line-height:74px}

/* features */
.features{height:203px;background:var(--soft);border-bottom:1px solid var(--line)}
.features .wrap{display:flex;gap:26px;padding-top:30px}
.feature{flex:1;display:flex;gap:16px}
.feature .ico{width:48px;height:48px;border-radius:50%;border:1px solid #d6d7d9;background:#fff;flex:none;display:flex;align-items:center;justify-content:center}
.feature h3{font-size:15px;font-weight:600;color:#2f3134;margin-bottom:6px}
.feature p{font-size:12px;color:var(--muted);line-height:1.55;min-height:56px}
.btn{display:inline-block;background:var(--accent);color:#fff;font-size:11px;font-weight:600;padding:7px 18px;border-bottom:2px solid var(--accent-dark);margin-top:10px}

/* section heading */
.heading{display:flex;align-items:center;gap:14px;font-size:15px;font-weight:600;color:#2f3134}
.heading::after{content:"";flex:1;height:6px;background:repeating-linear-gradient(180deg,#eaebec 0 1px,transparent 1px 3px)}

/* recent work */
.work{padding-top:40px}
.work .grid{display:flex;gap:22px;margin-top:20px}
.work figure{flex:1;text-align:center}
.work .shot{height:188px}
.shot.a{background:linear-gradient(135deg,#c9d9ea,#6f8eb5)}
.shot.b{background:linear-gradient(135deg,#f5e3b4,#6f8aa8)}
.shot.c{background:linear-gradient(135deg,#1b3c8e,#0b1d57)}
.work figcaption{margin-top:14px;font-size:13px;font-weight:600;color:#333}
.work small{display:block;font-size:11px;color:var(--faint)}

/* about + unique */
.info{display:flex;gap:36px;margin-top:60px}
.info .col{flex:1}
.tabs{display:flex;margin-top:18px;border:1px solid var(--line);border-bottom:none}
.tabs span{flex:1;text-align:center;font-size:11px;font-weight:600;color:#444;padding:8px 0;border-right:1px solid var(--line);background:#fafafa}
.tabs span:last-child{border-right:none}
.tabs span.on{background:#fff;border-top:2px solid var(--accent)}
.about p{font-size:12px;color:var(--muted);line-height:1.72;margin-top:14px}
.checks{list-style:none;margin-top:18px}
.checks li{display:flex;gap:10px;font-size:12px;color:var(--muted);line-height:1.55;margin-bottom:9px}
.checks li svg{flex:none;margin-top:1px}
.checks b{color:#2f3134;font-weight:700}

/* audit */
.audit{margin-top:40px;border:1px solid var(--line);border-left:3px solid var(--accent);height:120px;display:flex;align-items:center;padding:0 26px;gap:30px}
.audit h3{font-size:17px;font-weight:600;color:#2f3134}
.audit p{font-size:11.5px;color:var(--muted);line-height:1.55;margin-top:4px}
.audit .btn{flex:none;padding:10px 20px;font-size:13px;margin:0}

/* clients */
.clients{margin-top:54px}
.clients .row{display:flex;justify-content:space-between;margin-top:30px;padding:0 10px}
.clients .row span{font-size:26px;font-weight:600;color:#b8babd}
.tip{position:absolute;left:30px;top:-24px;background:#2f3134;color:#fff;font-size:10px;padding:2px 8px}

/* footer */
.footer{position:absolute;left:0;right:0;top:1840px;height:323px;background:#f3f3f3;border-top:1px solid var(--line)}
.footer .wrap{display:flex;padding-top:30px}
.footer h4{font-size:10.5px;font-weight:700;color:#2f3134;text-transform:uppercase;margin-bottom:14px}
.footer .bottomline h3{font-size:19px;font-weight:600;margin-bottom:10px}
.footer .bottomline a{display:block;font-size:11px;color:#444;line-height:2.05}
.bottomline{width:225px}
.tweets{width:228px}
.tweet{display:flex;gap:10px;margin-bottom:18px;font-size:11px;color:#555;line-height:1.55}
.tweet a{color:var(--accent)}
.tweet em{display:block;font-size:9px;color:#888}
.form input,.form textarea{display:block;width:205px;border:1px solid #d8d9db;background:#fff;font:italic 10.5px "Open Sans",sans-serif;color:#aaa;padding:6px 8px 6px 26px;margin-bottom:12px}
.form textarea{height:96px;resize:none}
.form .btn{margin-top:0;padding:7px 24px}

/* bottom bar */
.bottombar{position:absolute;left:0;right:0;top:2163px;height:56px;background:var(--bar);color:#9da0a4;font-size:10.5px}
.bottombar .wrap{display:flex;justify-content:space-between;align-items:center;height:56px}
.bottombar b{color:#fff;font-weight:600}
.totop{position:absolute;right:30px;width:38px;height:38px;background:#595c60;display:flex;align-items:center;justify-content:center}
</style>
</head>
<body>

<div class="topbar">
  <div class="wrap">
    <span>Brightwell Power Systems</span>
    <div class="contact">
      <span>Call us: <b>1-855-262-4410</b></span>
      <div class="social"><span></span><span></span><span></span><span></span><span></span><span></span><span></span></div>
    </div>
  </div>
</div>

<div class="settings" style="top:28px"><svg width="16" height="16" viewBox="0 0 16 16"><circle cx="8" cy="8" r="6" fill="none" stroke="#fff" stroke-width="3" stroke-dasharray="3 1.7"/><circle cx="8" cy="8" r="2" fill="#fff"/></svg></div>

<header class="nav">
  <div class="wrap">
    <div class="brand"><i></i>Brightwell</div>
    <nav class="menu">
      <a class="active">Home</a><a>About Us</a><a>Portfolio</a><a>Why LED?</a><a>FAQ</a><a>Contact Us</a>
    </nav>
  </div>
</header>

<section class="hero">
  <div class="wrap">
    <h1>LED Lighting Solutions</h1>
    <p>How Can You Save on Your Energy Bill?</p>
    <div class="lamps" role="img" aria-label="Photograph of assorted LED bulbs and spotlights"></div>
  </div>
  <div class="arrow prev"><svg width="8" height="12"><path d="M7 1 2 6l5 5" stroke="#fff" stroke-width="2" fill="none"/></svg></div>
  <div class="arrow next"><svg width="8" height="12"><path d="M1 1l5 5-5 5" stroke="#fff" stroke-width="2" fill="none"/></svg></div>
  <div class="dots"><span></span><span></span><span></span><span class="on"></span></div>
</section>

<div class="tagline"><div class="wrap">Brightwell Power Systems is an acknowledged Green Energy leader providing energy saving lighting solutions....</div></div>
<div class="settings" style="top:530px"><svg width="16" height="16" viewBox="0 0 16 16"><circle cx="8" cy="8" r="6" fill="none" stroke="#fff" stroke-width="3" stroke-dasharray="3 1.7"/><circle cx="8" cy="8" r="2" fill="#fff"/></svg></div>

<section class="features">
  <div class="wrap">
    <div class="feature">
      <div class="ico"><svg width="16" height="18"><circle cx="8" cy="5" r="4" fill="#444"/><path d="M1 18c0-6 14-6 14 0z" fill="#444"/></svg></div>
      <div><h3>Smart Energy Solutions</h3><p>Brightwell Products leads the way in smart energy solutions for its clients.</p><a class="btn">Read More</a></div>
    </div>
    <div class="feature">
      <div class="ico"><svg width="16" height="18"><circle cx="8" cy="5" r="4" fill="#444"/><path d="M1 18c0-6 14-6 14 0z" fill="#444"/></svg></div>
      <div><h3>Energy Efficiency</h3><p>LEDs are up to 90% more energy efficient than conventional lighting sources.</p><a class="btn">Read More</a></div>
    </div>
    <div class="feature">
      <div class="ico"><svg width="16" height="18"><circle cx="8" cy="5" r="4" fill="#444"/><path d="M1 18c0-6 14-6 14 0z" fill="#444"/></svg></div>
      <div><h3>Durability</h3><p>LEDs contain no moving parts or fragile filaments. Being that they're solid state components, they are difficult to damage with external shock</p><a class="btn">Read More</a></div>
    </div>
  </div>
</section>

<main class="wrap">
  <section class="work">
    <h2 class="heading">Recent Work</h2>
    <div class="grid">
      <figure><div class="shot a" role="img" aria-label="Photograph of LED spotlight bulbs against a blue building"></div><figcaption>Brightwell Power Systems<small>LED Bulbs</small></figcaption></figure>
      <figure><div class="shot b" role="img" aria-label="Photograph of LED tube lights"></div><figcaption>Brightwell Power Systems<small>LED tube lights</small></figcaption></figure>
      <figure><div class="shot c" role="img" aria-label="Photograph of LED bulbs on a dark blue background"></div><figcaption>Brightwell Power Systems<small>LED Bulbs</small></figcaption></figure>
    </div>
  </section>

  <section class="info">
    <div class="col about">
      <h2 class="heading">About US</h2>
      <div class="tabs"><span>Company</span><span class="on">Who We Are</span><span>Energy Audit</span></div>
      <p>Brightwell Power Systems is an acknowledged Green Energy leader providing energy saving lighting solutions. Our GBPA trained professionals coupled with our close relationships with the leading LED manufacturers around the world, ensures that your LED retrofit project will be affordable; saving you up to 75% on your lighting costs and drastically reducing replacement costs. Our turn-key system takes care of everything from the initial lighting energy audit, to an energy savWhy We Are Uniqueing solution, to professional installation, and finally complete cleanup and proper disposal.</p>
    </div>
    <div class="col">
      <h2 class="heading">Why We Are Unique</h2>
      <ul class="checks">
        <li><svg width="14" height="14"><circle cx="7" cy="7" r="7" fill="var(--accent)"/><path d="M4 7l2 2 4-4" stroke="#fff" stroke-width="1.6" fill="none"/></svg><span>Established in 1986 with 25 years of outstanding service, a <b>FSP approved vendor</b></span></li>
        <li><svg width="14" height="14"><circle cx="7" cy="7" r="7" fill="var(--accent)"/><path d="M4 7l2 2 4-4" stroke="#fff" stroke-width="1.6" fill="none"/></svg><span>A <b>Service-Disabled Veteran-Owned</b> company focused on hiring Service Disabled Veterans, Veterans and family members of veterans</span></li>
        <li><svg width="14" height="14"><circle cx="7" cy="7" r="7" fill="var(--accent)"/><path d="M4 7l2 2 4-4" stroke="#fff" stroke-width="1.6" fill="none"/></svg><span>As a member of the <b>National Green Building Alliance</b>, we support green design, construction and operations</span></li>
        <li><svg width="14" height="14"><circle cx="7" cy="7" r="7" fill="var(--accent)"/><path d="M4 7l2 2 4-4" stroke="#fff" stroke-width="1.6" fill="none"/></svg><span><b>GBPA</b> (Green Building Practice Accredited) trained employees</span></li>
        <li><svg width="14" height="14"><circle cx="7" cy="7" r="7" fill="var(--accent)"/><path d="M4 7l2 2 4-4" stroke="#fff" stroke-width="1.6" fill="none"/></svg><span><b>DUNS Number</b> - 284613907</span></li>
        <li><svg width="14" height="14"><circle cx="7" cy="7" r="7" fill="var(--accent)"/><path d="M4 7l2 2 4-4" stroke="#fff" stroke-width="1.6" fill="none"/></svg><span><b>CAGE Code</b> - 7K2R9</span></li>
        <li><svg width="14" height="14"><circle cx="7" cy="7" r="7" fill="var(--accent)"/><path d="M4 7l2 2 4-4" stroke="#fff" stroke-width="1.6" fill="none"/></svg><span>Active in System for Award Management (<b>SAM</b>) - Registration valid until 07/15/2014</span></li>
        <li><svg width="14" height="14"><circle cx="7" cy="7" r="7" fill="var(--accent)"/><path d="M4 7l2 2 4-4" stroke="#fff" stroke-width="1.6" fill="none"/></svg><span>Registered <b>NAICS</b> codes - 238210, 335110, 335122</span></li>
        <li><svg width="14" height="14"><circle cx="7" cy="7" r="7" fill="var(--accent)"/><path d="M4 7l2 2 4-4" stroke="#fff" stroke-width="1.6" fill="none"/></svg><span>LED products available on <b>FSP Schedule - FS-22P-4418M</b></span></li>
      </ul>
    </div>
  </section>

  <section class="audit">
    <div>
      <h3>Request a Free, No Obligation Energy Audit</h3>
      <p>Fill your information in Contact form to receive a free audit of your current lighting system. There is no cost or obligation and when we are done you'll know how much money and energy you can save by switching to an LED lighting solution. We will contact you within 24 hours of receiving your request.</p>
    </div>
    <a class="btn">Read More!</a>
  </section>

  <section class="clients" style="position:relative">
    <span class="tip">Sed ut perspiciatis</span>
    <h2 class="heading">Our Clients</h2>
    <div class="row"><span>Halvern</span><span>Tidewell</span><span>Corbin</span><span>Northgate</span><span>Verano</span></div>
  </section>
</main>

<div class="totop" style="top:1052px"><svg width="10" height="7"><path d="M1 6l4-4 4 4" stroke="#fff" stroke-width="1.6" fill="none"/></svg></div>
<div class="totop" style="top:1653px;height:12px"></div>

<footer class="footer">
  <div class="wrap">
    <div class="bottomline">
      <h3>The Bottom Line</h3>
      <a>The Savings</a><a>LED Retrofit Process</a><a>Tax Incentives</a><a>Utility Rebates</a>
    </div>
    <div class="tweets">
      <h4>Latest Tweets</h4>
      <div class="tweet"><svg width="12" height="10"><path d="M0 8c4 1 8-1 9-6l3-1-2 2C9 8 4 11 0 8z" fill="#999"/></svg><div>Sed ut perspiciatis unde omnis iste natus error sit voluptatem <a>http://brightfeed.net</a><em>Jan 7, 2013</em></div></div>
      <div class="tweet"><svg width="12" height="10"><path d="M0 8c4 1 8-1 9-6l3-1-2 2C9 8 4 11 0 8z" fill="#999"/></svg><div>Nemo enim ipsam voluptatem quia voluptas sit aspernatur aliquid :) <a>http://brightfeed.net</a><em>Jan 7, 2013</em></div></div>
    </div>
    <div class="form">
      <h4>Contact Form</h4>
      <input value="Name (required)" aria-label="Name">
      <input value="E-mail (required)" aria-label="E-mail">
      <textarea aria-label="Message">Message</textarea>
      <a class="btn">Send</a>
    </div>
  </div>
</footer>

<div class="bottombar">
  <div class="wrap">
    <span>Copyright © 2014 <b>brightwell power systems</b>. All Right Reserved.</span>
    <span style="display:flex;gap:10px;align-items:center">Follow Us <span class="social"><span></span><span></span><span></span><span></span><span></span><span></span></span></span>
  </div>
  <div class="totop" style="top:-10px"><svg width="10" height="7"><path d="M1 6l4-4 4 4" stroke="#fff" stroke-width="1.6" fill="none"/></svg></div>
</div>

</body>
</html>
```